Design a Site That Says: ‘This is the Next Big Thing in Defense Tech

We are redesigning the Torvane Aircraft website to deliver a bold, high-impact digital experience that convinces on-the-fence investors this is the moment to get involved. The site must feel fast-moving, technology-forward, and unlike anything coming out of traditional aerospace — no more beige PDFs or outdated defense branding. It should reflect the precision, autonomy, and scale of our product without revealing the proprietary details. Through sleek, modern visuals, sharp messaging, and subtle cues of aerospace innovation — airport runways, carbon fiber textures, night imagery, and mission-ready tone — we want to guide the audience toward one powerful conclusion: Torvane Aircraft is building the future of autonomous defense aviation, and the time to invest is now.
✈️ What Is Torvane Aircraft?
Torvane Aircraft is a next-generation autonomous aerial system built for the future of defense. Where legacy drones were designed for one-off missions and slow production pipelines, Torvane is built from the ground up for speed, scalability, and autonomy. Its sleek, tailless design reflects not just a new aircraft, but a new philosophy: one where performance, flexibility, and manufacturing efficiency converge.

This is not another iteration — it’s a complete rethink of how unmanned systems should be built, deployed, and scaled.

🧩 Competitive Discriminators
1. Production-First Philosophy
Most aircraft are built like custom machines. Torvane is different — it’s engineered for rapid production using cutting-edge methods adapted from high-rate industries. This isn’t just about speed — it’s about being able to respond to demand in real time.

2. Autonomy at the Core
Torvane doesn’t rely on ground crews or remote pilots. It’s built for full autonomy — to operate as a single asset or as part of a larger, coordinated swarm without micromanagement.

3. Modularity Without Compromise
One airframe. Many missions. With a modular internal architecture, Torvane can be adapted to a wide range of operational roles without altering its core structure — or its production rhythm.

4. Clean Configuration, Internal Systems
Everything is housed inside — systems, sensors, payloads — resulting in a streamlined platform that looks and performs differently from the start.

5. Distinct Visual Signature
From its tailless form to its smooth composite surfaces, Torvane Aircraft looks like the future — because it is. It’s what happens when aerospace engineers design without compromise.

👀 What Will Stand Out — Even to a Casual Observer
It doesn’t look like any drone they’ve seen before.
No tail, no hardpoints, no draggy silhouettes — just smooth geometry and silent confidence.

It feels like it belongs to the next generation.
While legacy platforms show their age, Torvane shows what’s next. It looks engineered, not assembled.

It invites imagination.
Observers can’t help but wonder: What’s inside? What can it do? How is it built so differently?

It feels like a system, not just an aircraft.
From design to production to deployment, everything about Torvane is intentional — and scalable.

```html
<!DOCTYPE html>
<html lang="en">
<head>
<meta charset="utf-8">
<title>Torvane Aircraft</title>
<link rel="stylesheet" href="https://fonts.googleapis.com/css2?family=Oswald:wght@400;500;600&family=Barlow:wght@400;500&display=swap">
<style>
:root{
  --navy:#0b2a4a;
  --navy-deep:#081f38;
  --blue:#0a3d6b;
  --ink:#1d1d1f;
  --text:#3b3f45;
  --muted:#6b7078;
  --white:#ffffff;
  --black:#000000;
  --pale:#e6f2fb;
  --btn-dark:#2d2d2d;
}
*{box-sizing:border-box;margin:0;padding:0}
html,body{width:1200px;height:3305px;overflow:hidden}
body{font-family:"Barlow",sans-serif;color:var(--text);background:var(--white);position:relative}
.abs{position:absolute}
.heading{font-family:"Oswald",sans-serif;font-weight:400;color:var(--ink)}

/* hero */
.hero{position:absolute;left:0;top:0;width:1200px;height:505px;
  background:linear-gradient(180deg,#2b3644 0%,#55606c 35%,#7c8088 60%,#9c8f80 85%,#6b6258 100%)}
.logo{position:absolute;left:173px;top:22px;display:flex;align-items:center;gap:10px;
  font-family:"Barlow",sans-serif;font-weight:500;font-size:28px;letter-spacing:4px;color:var(--white)}
.logo .dot{width:14px;height:14px;border-radius:50%;background:var(--white)}
.nav{position:absolute;top:22px;left:611px;display:flex;align-items:center;gap:27px;font-size:14px;color:var(--white)}
.nav .members{background:#2a2a2a;padding:9px 16px;margin-left:8px}
.search{position:absolute;left:1012px;top:30px}
.hero .tagline{position:absolute;top:150px;left:0;width:1200px;text-align:center;color:var(--white);font-size:17px;line-height:21px}
.hero h1{position:absolute;top:218px;left:0;width:1200px;text-align:center;color:var(--white);
  font-family:"Oswald",sans-serif;font-weight:500;font-size:54px;line-height:70px}
.btn-light{position:absolute;left:536px;top:382px;width:127px;height:35px;background:var(--white);color:var(--ink);
  font-size:14px;display:flex;align-items:center;justify-content:center;letter-spacing:.3px}
.band{position:absolute;top:505px;left:0;width:1200px;height:135px;background:var(--black);color:var(--white);
  font-family:"Oswald",sans-serif;font-weight:600;font-size:84px;display:flex;align-items:center;justify-content:center;letter-spacing:1px}

/* focuses */
.section-title{position:absolute;left:0;width:1200px;text-align:center;font-size:37px}
.card{position:absolute;width:275px;background:var(--white);border-radius:6px;box-shadow:0 2px 10px rgba(0,0,0,.08);padding:18px 18px 0}
.card .top{display:flex;gap:18px;align-items:flex-start}
.icon{width:53px;height:53px;border-radius:50%;background:var(--navy);flex:none;display:flex;align-items:center;justify-content:center}
.card h3{font-family:"Oswald",sans-serif;font-weight:400;font-size:20px;line-height:29px;color:var(--ink);margin-top:1px}
.card p{font-size:13px;line-height:17px;margin-top:24px;color:var(--text)}

/* about */
.about{position:absolute;top:1292px;left:0;width:1200px;height:462px;
  background:linear-gradient(120deg,#8f8d8c 0%,#d8d6d4 22%,#f1efee 45%,#e9ecef 70%,#c9cdd2 100%)}
.about-panel{position:absolute;left:169px;top:90px;width:480px;height:270px;background:rgba(255,255,255,.35);border-radius:6px}
.about h2{position:absolute;left:187px;top:118px;font-size:36px}
.about h2 span{color:var(--blue)}
.about p{position:absolute;left:187px;top:190px;width:460px;font-size:13.5px;line-height:19.3px;color:var(--ink)}
.btn-navy{position:absolute;background:var(--blue);color:var(--white);font-size:14px;display:flex;align-items:center;justify-content:center}
.plane{position:absolute;left:700px;top:150px;width:170px;height:140px;border-radius:50%;
  background:radial-gradient(ellipse,#d9b2ab 0%,rgba(220,190,185,0) 70%)}

/* mission / vision */
.stripe{position:absolute;left:740px;top:1754px;width:460px;height:647px}
.photo{position:absolute}
.mv h3{position:absolute;font-size:26px}
.mv p{position:absolute;width:400px;font-size:15px;line-height:19.5px;color:var(--ink)}
.btn-dark{position:absolute;width:104px;height:35px;background:var(--btn-dark);color:var(--white);font-size:14px;display:flex;align-items:center;justify-content:center}

/* blogs */
.blogs{position:absolute;top:2401px;left:0;width:1200px;height:680px;background:var(--pale)}
.blogs h2{position:absolute;left:253px;top:80px;font-size:37px;color:var(--blue);font-weight:500}
.post{position:absolute;top:147px;width:275px;height:382px;background:var(--white);border-radius:10px;overflow:hidden}
.post .img{height:191px}
.post .body{padding:12px 18px}
.post .author{font-size:11.5px;color:var(--muted)}
.post h3{font-family:"Oswald",sans-serif;font-weight:500;font-size:17px;color:var(--blue);margin-top:6px}
.post p{font-size:12.5px;line-height:16.5px;color:var(--ink);margin-top:12px}
.post .more{font-size:11.5px;color:var(--blue);margin-top:14px}

/* footer */
.footer{position:absolute;left:0;top:2970px;width:1200px;height:335px}
.footer .logo-foot{position:absolute;left:170px;top:138px;font-size:28px;letter-spacing:4px;color:var(--white);font-weight:500;display:flex;align-items:center;gap:10px}
.footer .logo-foot .dot{width:14px;height:14px;border-radius:50%;background:#4a90d9}
.socials{position:absolute;left:182px;top:217px;display:flex;gap:17px}
.socials span{width:25px;height:25px;border-radius:50%;background:var(--white)}
.footer h4{position:absolute;font-family:"Oswald",sans-serif;font-weight:500;font-size:21px;color:var(--white)}
.links{position:absolute;left:485px;top:164px;list-style:none;font-size:13.5px;color:#c7d3e0;line-height:28px}
.contact-row{position:absolute;left:755px;display:flex;gap:13px;font-size:13.5px;color:#c7d3e0;line-height:18px}
.contact-row .ic{width:24px;height:24px;border-radius:50%;background:var(--white);flex:none;display:flex;align-items:center;justify-content:center}
</style>
</head>
<body>

<header class="hero" role="img" aria-label="Photograph of a tailless aircraft wing seen from below against a dramatic cloudy sky">
  <div class="logo"><span class="dot"></span>TORVANE</div>
  <nav class="nav"><span>Home</span><span>About</span><span>Contact</span><span>Blog</span><span class="members">Members Area</span></nav>
  <svg class="search" width="18" height="18" viewBox="0 0 18 18"><circle cx="7.5" cy="7.5" r="5.5" fill="none" stroke="#fff" stroke-width="2"/><line x1="11.5" y1="11.5" x2="16" y2="16" stroke="#fff" stroke-width="2.4" stroke-linecap="round"/></svg>
  <p class="tagline">Enhancing Warfighter Capability, Driving Affordability,<br>Powering Scalable Innovation</p>
  <h1>Revolutionary Capability,<br>Evolutionary Technology</h1>
  <span class="btn-light">EXPLORE MORE</span>
</header>
<div class="band">BUILT | DEPLOYED | SCALED</div>

<section class="focuses">
  <h2 class="heading section-title" style="top:705px">Strategic Innovation Focuses</h2>

  <article class="card" style="left:169px;top:798px;height:194px">
    <div class="top"><span class="icon"><svg width="26" height="26" viewBox="0 0 26 26" fill="none" stroke="#fff" stroke-width="1.4"><path d="M3 9l10-5 10 5-10 5z"/><path d="M3 13l10 5 10-5"/><path d="M3 17l10 5 10-5"/></svg></span><h3>Rapid<br>Airframes</h3></div>
    <p>Torvane Aircraft is revolutionizing composite production for aerospace structures by cutting fabrication and assembly times, minimizing labor,</p>
  </article>
  <article class="card" style="left:461px;top:798px;height:194px">
    <div class="top"><span class="icon"><svg width="26" height="26" viewBox="0 0 26 26" fill="none" stroke="#fff" stroke-width="1.4"><circle cx="13" cy="10" r="5"/><path d="M4 22h18M8 22l2-7M18 22l-2-7"/></svg></span><h3>Avionics<br>Architecture</h3></div>
    <p>We are optimizing the avionics architecture by streamlining its complexity, developing a modular, product-agnostic computing framework with integrated redundancy</p>
  </article>
  <article class="card" style="left:752px;top:798px;height:194px">
    <div class="top"><span class="icon"><svg width="26" height="26" viewBox="0 0 26 26" fill="none" stroke="#fff" stroke-width="1.4"><circle cx="13" cy="13" r="10"/><circle cx="13" cy="13" r="6"/><circle cx="13" cy="13" r="2"/></svg></span><h3>Attritable<br>Propulsion</h3></div>
    <p>We are developing a high-performance class of engine systems that are manufacturable, easily swappable, and designed for streamlined maintenance</p>
  </article>
  <article class="card" style="left:169px;top:1027px;height:178px">
    <div class="top"><span class="icon"><svg width="26" height="26" viewBox="0 0 26 26" fill="none" stroke="#fff" stroke-width="1.4"><rect x="8" y="8" width="10" height="10"/><path d="M11 3v5M15 3v5M11 18v5M15 18v5M3 11h5M3 15h5M18 11h5M18 15h5"/></svg></span><h3>Artificial<br>Intelligence</h3></div>
    <p>We are developing a high-performance class of engine systems that are manufacturable, easily swappable, and designed for streamlined maintenance</p>
  </article>
  <article class="card" style="left:461px;top:1027px;height:178px">
    <div class="top"><span class="icon"><svg width="26" height="26" viewBox="0 0 26 26" fill="none" stroke="#fff" stroke-width="1.4"><path d="M2 18l11-9 11 9-11-3z"/></svg></span><h3>Spiral Development<br>Aircraft</h3></div>
    <p>We are developing a high-performance class of engine systems that are manufacturable, easily swappable, and designed for streamlined maintenance</p>
  </article>
  <article class="card" style="left:752px;top:1027px;height:178px">
    <div class="top"><span class="icon"><svg width="26" height="26" viewBox="0 0 26 26" fill="none" stroke="#fff" stroke-width="1.4"><rect x="5" y="9" width="16" height="11" rx="3"/><circle cx="10" cy="14.5" r="1.5"/><circle cx="16" cy="14.5" r="1.5"/><path d="M13 9V4"/></svg></span><h3>Automated Ground<br>Operations</h3></div>
    <p>We are developing a high-performance class of engine systems that are manufacturable, easily swappable, and designed for streamlined maintenance</p>
  </article>
</section>

<section class="about" role="img" aria-label="Photograph of an airliner flying overhead framed by curved modern terminal architecture">
  <div class="about-panel"></div>
  <div class="plane"></div>
  <h2 class="heading">About <span>TORVANE AIRCRAFT</span></h2>
  <p>Torvane Aircraft, a visionary aerospace engineering firm, was established in 2024 with a core focus on integrating state-of-the-art technologies into Unmanned Aerial Systems (UAS). Our commitment to seamless adoption of cutting-edge advancements distinguishes us, catering to aircraft enthusiasts, aerospace defense, and engineering professionals.</p>
  <span class="btn-navy" style="left:187px;top:312px;width:127px;height:35px">EXPLORE MORE</span>
</section>

<section class="mv">
  <svg class="stripe" viewBox="0 0 460 647" aria-hidden="true"><polygon points="460,0 460,130 203,647 0,647" fill="#e3e8ec"/></svg>
  <div class="photo" style="left:169px;top:1843px;width:423px;height:280px;background:linear-gradient(135deg,#1f3f66,#2d8bd6 50%,#c9b9a7)" role="img" aria-label="Illustration of an aircraft on a glowing circuit board surrounded by electronics"></div>
  <div class="photo" style="left:609px;top:1843px;width:424px;height:280px;background:linear-gradient(135deg,#8ea3b8,#3f5e7d 55%,#1f3550)" role="img" aria-label="Illustration of an engineer at a console overlooking a jet in an aircraft factory"></div>
  <h3 class="heading" style="left:263px;top:2140px">Mission</h3>
  <p style="left:187px;top:2200px">Torvane Aircraft is revolutionizing the aerospace industry with fully autonomous aerial vehicles, seamlessly integrating proven technologies</p>
  <span class="btn-dark" style="left:187px;top:2278px">READ MORE</span>
  <h3 class="heading" style="left:703px;top:2140px">Vision</h3>
  <p style="left:626px;top:2200px">To transform the aerospace industry by harnessing the best innovations and maximizing every dollar to shape a future where aerospace is defined</p>
  <span class="btn-dark" style="left:626px;top:2278px">READ MORE</span>
</section>

<section class="blogs">
  <h2 class="heading">Our Blogs</h2>
  <article class="post" style="left:169px">
    <div class="img" style="background:linear-gradient(160deg,#0a1a35,#1d4a7a 60%,#0a1a35)" role="img" aria-label="Technical illustration of a tailless aircraft with labelled subsystems"></div>
    <div class="body"><div class="author">Dale Marsh</div><h3>Where It All Begins</h3><p>After a short break, we're back with another installment of the Torvane Aircraft blog series, diving deeper into the new space approach</p><div class="more">- Read More</div></div>
  </article>
  <article class="post" style="left:463px">
    <div class="img" style="background:linear-gradient(180deg,#5d5a45,#3e3d33 60%,#c8c6c2)" role="img" aria-label="Photograph of a person standing beside a large rocket stage in a hangar"></div>
    <div class="body"><div class="author">Dale Marsh</div><h3>Why I Believe I Can</h3><p>This is my story, about how a kid with the "Knack" that wanted to work on cars, sent something to space, the moon, and is now taking on Aerospace.</p><div class="more">- Read More</div></div>
  </article>
  <article class="post" style="left:756px">
    <div class="img" style="background:linear-gradient(180deg,#9fb3c8,#e3e9ef 60%,#b7c3cf)" role="img" aria-label="Illustration of an unmanned aircraft flying above clouds"></div>
    <div class="body"><div class="author">Dale Marsh</div><h3>Introducing Torvane Aircraft</h3><p>Torvane Aircraft is an aerospace technology company dedicated to transforming how aerospace innovation happens.</p><div class="more">- Read More</div></div>
  </article>
</section>

<footer class="footer">
  <svg class="abs" style="left:0;top:0" width="1200" height="335" viewBox="0 0 1200 335" aria-hidden="true"><polygon points="0,85 600,0 1200,85 1200,335 0,335" fill="#071f36"/></svg>
  <div class="logo-foot"><span class="dot"></span>TORVANE</div>
  <div class="socials"><span></span><span></span><span></span></div>
  <h4 style="left:485px;top:115px">Quick Links</h4>
  <ul class="links"><li>Home</li><li>About</li><li>Contact</li><li>Blog</li><li>Members Area</li></ul>
  <h4 style="left:755px;top:115px">Contact</h4>
  <div class="contact-row" style="top:173px"><span class="ic"><svg width="12" height="10" viewBox="0 0 12 10"><rect x="0.5" y="0.5" width="11" height="9" fill="none" stroke="#071f36"/><path d="M0.5 0.5l5.5 5 5.5-5" fill="none" stroke="#071f36"/></svg></span><span>info@torvaneaircraft.com</span></div>
  <div class="contact-row" style="top:213px"><span class="ic" style="margin-top:8px"><svg width="10" height="14" viewBox="0 0 10 14"><path d="M5 13.5C2 9 0.5 6.8 0.5 5a4.5 4.5 0 019 0c0 1.8-1.5 4-4.5 8.5z" fill="#071f36"/><circle cx="5" cy="5" r="1.6" fill="#fff"/></svg></span><span>Torvane Aircraft Inc.<br>4820 Halden Ridge Road, Austin, Texas<br>78730</span></div>
</footer>

</body>
</html>
```